New Template design for Website in Wordpress

We are interested in changing our website look at www.haulvantix.com -We also are very interested in Have it done in Wordpress in which we are understanding the search engines are liking a bit more. The website we would want to try working with on this is www.haulvantix.com. We look forward to seeing the different design ideas please just make sure they are in wordpress! Thanks, Merrick

Reason: need more design idea..... We would still like to use our pictures off our site since we paid for them so keep that in mind as well as we would still want the rotating pictures in the head of the page but not in Flash.

```html
<!DOCTYPE html>
<html lang="en">
<head>
<meta charset="utf-8">
<title>Haulvantix — A Diversified Freight Company</title>
<link href="https://fonts.googleapis.com/css2?family=Open+Sans:ital,wght@0,400;0,600;0,700;1,400;1,600&display=swap" rel="stylesheet">
<style>
:root{
  --dark:#161616;
  --footer:#2a2a2a;
  --orange:#f7a21b;
  --orange-light:#ffc24a;
  --blue:#1a8fd6;
  --blue-nav:#1f8ccc;
  --text:#7a7a7a;
  --heading:#1e1e1e;
  --page:#f4f4f4;
  --white:#ffffff;
}
*{box-sizing:border-box;margin:0;padding:0}
html,body{width:970px;height:1200px;overflow:hidden}
body{font-family:"Open Sans",sans-serif;background:var(--page);position:relative;color:var(--text)}
.abs{position:absolute}

.site-header{left:0;top:0;width:970px;height:122px;background:var(--dark)}
.brand{left:96px;top:26px;display:flex;align-items:center;gap:10px}
.brand-mark{width:52px;height:48px;background:var(--blue);border-radius:6px}
.brand-name{font-size:27px;font-weight:700;color:var(--orange);line-height:1;letter-spacing:.5px}
.brand-tag{font-size:11.5px;color:#bdbdbd;margin-top:4px}
.hotline{right:98px;top:26px;display:flex;gap:8px;align-items:center}
.hotline-label{color:var(--orange);font-size:14px;font-weight:600;text-align:right}
.hotline-number{color:#d8d8d8;font-size:17px;font-weight:600;font-style:italic;text-align:right}

.main-nav{left:96px;top:98px;height:45px;display:flex;z-index:3}
.main-nav a{display:block;height:45px;line-height:45px;padding:0 15px;font-size:14.5px;color:#4a4a4a;text-decoration:none;background:linear-gradient(#cfcfcf,#b2b2b2);border-right:1px solid #9f9f9f}
.main-nav a.current{background:linear-gradient(var(--orange-light),var(--orange));color:#1e1e1e}
.main-nav a.quote{background:var(--blue-nav);color:#fff;padding:0 15px;border:none}

.hero{left:0;top:122px;width:970px;height:575px;background:linear-gradient(180deg,#9fb6c9 0%,#cdb88a 45%,#c8a45e 60%,#56708a 100%)}

.service-card{top:438px;width:178px;height:236px;background:var(--white);overflow:hidden}
.card-photo{height:118px}
.card-body{padding:14px 12px 0 15px}
.card-title{font-size:13px;font-weight:600;color:var(--heading);margin-bottom:9px;white-space:nowrap}
.card-text{font-size:10px;line-height:15.5px;color:#777}
.card-more{display:block;margin-top:6px;font-size:9.5px;font-weight:700;color:var(--blue);text-decoration:none}

.intro{left:96px;top:720px;width:522px}
.intro h1{font-size:19.5px;font-weight:700;color:var(--blue);letter-spacing:.2px}
.intro h2{font-size:12.5px;font-weight:400;color:#9a9a9a;margin-top:2px}
.rule{width:110px;height:2px;background:#c9c9c9;margin:10px 0 14px}
.intro p{font-size:10px;line-height:17px;text-align:justify;margin-bottom:6px}
.callout{font-size:12.5px;font-style:italic;font-weight:600;color:var(--heading);line-height:15.5px;margin-top:6px}
.callout a{color:var(--blue);font-weight:400;text-decoration:none}

.news{left:95px;top:990px;width:522px}
.news h3{font-size:19.5px;font-weight:600;color:var(--blue)}
.news-list{display:flex}
.news-item{width:187px}
.news-date{font-size:11.5px;font-weight:600;color:var(--orange)}
.news-title{font-size:10.5px;color:var(--blue);margin:10px 0 6px}
.news-text{font-size:9px;line-height:14px;color:#888}

.sidebar{left:654px;top:726px;width:209px;background:var(--white);box-shadow:0 0 4px rgba(0,0,0,.15)}
.sidebar-head{height:31px;background:linear-gradient(var(--orange-light),var(--orange));border-radius:4px 4px 0 0;font-size:15px;font-weight:700;color:var(--heading);padding:5px 12px}
.side-item{height:31px;border-bottom:1px solid #ddd;font-size:11px;font-weight:600;color:var(--heading);display:flex;align-items:center;gap:6px;padding-left:5px}
.side-item.open{color:var(--blue)}
.side-sub{padding:4px 0 10px 20px;border-bottom:1px solid #ddd}
.side-sub li{list-style:none;font-size:10px;color:#555;height:26.4px;line-height:26.4px}
.bullet{width:12px;height:12px;border-radius:50%;background:#555;display:inline-flex;align-items:center;justify-content:center;color:#fff;font-size:10px;line-height:1}

.site-footer{left:0;top:1138px;width:970px;height:62px;background:var(--footer)}
.footer-links{left:95px;top:12px;font-size:10px;color:#aaa}
.copyright{left:95px;top:37px;font-size:10px;color:#999}
.social{right:100px;top:22px;display:flex;gap:11px}
.social span{width:28px;height:28px;border-radius:50%;background:#555}
.social span.first{background:#2c5cbf}
</style>
</head>
<body>

<header class="site-header abs">
  <div class="brand abs">
    <div class="brand-mark"></div>
    <div>
      <div class="brand-name">HAULVANTIX</div>
      <div class="brand-tag">A DIVERSIFIED FREIGHT COMPANY</div>
    </div>
  </div>
  <div class="hotline abs">
    <svg width="36" height="40" viewBox="0 0 36 40"><rect x="2" y="2" width="20" height="32" rx="3" fill="none" stroke="#8a8a8a" stroke-width="3"/><path d="M14 20 l10 8 l8 -2 l-2 12 l-14 0 z" fill="#8a8a8a"/></svg>
    <div>
      <div class="hotline-label">7 DAYS WEEK CALL</div>
      <div class="hotline-number">(888) 555-0142</div>
    </div>
  </div>
</header>

<nav class="main-nav abs">
  <a class="current" href="#">HOME</a>
  <a href="#">ABOUT US</a>
  <a href="#">SERVICES</a>
  <a href="#">INSURANCE &amp; LEGAL INFO</a>
  <a href="#">CONATCT US</a>
  <a class="quote" href="#">FAST FREIGHT QUOTE</a>
</nav>

<div class="hero abs" role="img" aria-label="Rotating header photo: cargo ship with yellow cranes and stacked shipping containers"></div>

<article class="service-card abs" style="left:96px">
  <div class="card-photo" role="img" aria-label="Yellow excavator loaded on a lowboy trailer" style="background:linear-gradient(#b9cde0,#c9a640)"></div>
  <div class="card-body">
    <div class="card-title">HEAVY HAUL</div>
    <div class="card-text">No Limits on Equipment Weight and Size - All Machinery or Equipment transported</div>
    <a class="card-more" href="#">READ MORE ›</a>
  </div>
</article>
<article class="service-card abs" style="left:296px">
  <div class="card-photo" role="img" aria-label="White semi truck with dry van trailer" style="background:linear-gradient(#c8d6e2,#9aa08c)"></div>
  <div class="card-body">
    <div class="card-title">DRY &amp; REFRIGERATED</div>
    <div class="card-text">Dry Van Freight Quotes servicing 48 States and Canada! We currently offer ....</div>
    <a class="card-more" href="#">READ MORE ›</a>
  </div>
</article>
<article class="service-card abs" style="left:496px">
  <div class="card-photo" role="img" aria-label="Blue truck hauling a flatbed load on a highway" style="background:linear-gradient(#8fa78a,#6f7b8c)"></div>
  <div class="card-body">
    <div class="card-title">FLATBED, STEP DECK</div>
    <div class="card-text">Flatbed Freight Quotes &amp; Transport Service Shipping LTL reight thoughout</div>
    <a class="card-more" href="#">READ MORE ›</a>
  </div>
</article>
<article class="service-card abs" style="left:695px">
  <div class="card-photo" role="img" aria-label="Container ship at sea loaded with colorful containers" style="background:linear-gradient(#c9d8e6,#3f6a96)"></div>
  <div class="card-body">
    <div class="card-title">FREIGHT FORWARDING</div>
    <div class="card-text">Get Fast &amp; Free Freight Quotes Now and Save Worldwide shipping- Ocean</div>
    <a class="card-more" href="#">READ MORE ›</a>
  </div>
</article>

<section class="intro abs">
  <h1>GET FAST &amp; FREE FREIGHT QUOTES NOW AND SAVE!!</h1>
  <h2>WORLDWIDE SHIPPING- OCEAN AND TRUCKING WITH NO LIMITS</h2>
  <div class="rule"></div>
  <p>Welcome to Haulvantix and Vantix Cargo Inc. We are a one stop solution logistics company servicing Worldwide with our Trucking and Ocean shipping service. In using our freight services, we will negotiate a competitive freight quote using over 5000 different carriers who are certified and contracted by us. We have all equipment types available daily, service all freight types, and have no limits Worldwide.</p>
  <p>Whether you need a freight quote for a full load, LTL/Partial load, or Oversized Machinery or Equipment, trucking and/or ocean shipment, we will take care of it. All your freight or equipment to be shipped will be covered in full by our insurance with no limitations to match its value. We manage the calls, the paperwork, and the headaches, and you get your freight moved with no hassles at a competitive shipping price!</p>
  <div class="callout">Get your <a href="#">freight quote online now</a> or call 888-555-0142 now and let some of the top carriers in the country compete for your business</div>
</section>

<section class="news abs">
  <h3>LATEST NEWS</h3>
  <div class="rule"></div>
  <div class="news-list">
    <div class="news-item"><div class="news-date">20. 07. 2014</div><div class="news-title">Lorem ipsum dolor amet</div><div class="news-text">Pellentesque semper efficiluctus.<br>Nulla semper tortor est</div></div>
    <div class="news-item"><div class="news-date">20. 07. 2014</div><div class="news-title">Lorem ipsum dolor amet</div><div class="news-text">Pellentesque semper efficiluctus.<br>Nulla semper tortor est</div></div>
    <div class="news-item"><div class="news-date">20. 07. 2014</div><div class="news-title">Lorem ipsum dolor amet</div><div class="news-text">Pellentesque semper efficiluctus.<br>Nulla semper tortor est</div></div>
  </div>
</section>

<aside class="sidebar abs">
  <div class="sidebar-head">OUR SERVICES</div>
  <div class="side-item"><span class="bullet">+</span>WORLDWIDE FREIGHT SERVICES</div>
  <div class="side-item open"><span class="bullet">–</span>FREIGHT - TRUCKING SERVICE</div>
  <ul class="side-sub">
    <li>› Heavy Equipment Hauling</li>
    <li>› LTL Freight Transport</li>
    <li>› Flatbed Transport</li>
    <li>› Step Deck Transport</li>
    <li>› Dry Van Transport</li>
    <li>› Refrigerated Transport</li>
    <li>› Power Only &amp; Towaway Transport</li>
  </ul>
  <div class="side-item"><span class="bullet">+</span>OCEAN SHIPPING SERVICES</div>
  <div class="side-item"><span class="bullet">+</span>WE SHIP IT ALL WORLDWIDE!</div>
  <div class="side-item" style="border-bottom:none"><span class="bullet">+</span>POPLULAR PAGES</div>
</aside>

<footer class="site-footer abs">
  <div class="footer-links abs">Equipment Transport &nbsp;/&nbsp; Equipment Hauling &nbsp;/&nbsp; Shipping Service Areas</div>
  <div class="copyright abs">Copyright © 2014 Haulvantix. All Right Reseved.</div>
  <div class="social abs"><span class="first"></span><span></span><span></span><span></span><span></span></div>
</footer>

</body>
</html>
```